SunMeadow Yoga Website Design

Business Logo - attached
5 pages being:
Home
About
Classes
Blog
Contact

Would like Scrolling webpage and yoga symbols to be used.

Must have's being:
Easy to navigate, Text needs to be able to be edited/updated, Enquire Now Links, More Information Links, be a secure site, SEO,

Please refer to attached document for the information for the body of the website.

Target Market(s)

Educators, Community Service, Health and Wellbeing, Mental Health

Industry/Entity Type

Yoga

Coding

Coded - Design and coding required

Number of Pages Required

5+ page

Font styles to use
Other font styles liked:
• Bella Bold BC

Colors
0094D4
00A9DD
6FCCEA
C7EBF8
E9F6FB
6B429C
8869AF
B7A5CE
E3DAEB
F3F0F8

Requirements
Must have
• Easy to navigate, Text needs to be able to be edited/updated, Enquire Now Links, More Information Links, be a secure site, SEO,
Nice to have
• Scrolling webpage, yoga symbols

```html
<!DOCTYPE html>
<html lang="en">
<head>
<meta charset="utf-8">
<title>SunMeadow Yoga</title>
<link rel="stylesheet" href="https://fonts.googleapis.com/css2?family=Libre+Caslon+Text:wght@400;700&family=Roboto:wght@400;500;700&display=swap">
<style>
:root{
  --purple:#5b1fd1;
  --purple-deep:#5a17cc;
  --purple-light:#8d4ee3;
  --blue:#00a6df;
  --ink:#1d1d1d;
  --text:#333;
  --white:#fff;
  --line:#cfcfcf;
  --footer:#000;
}
*{box-sizing:border-box;margin:0;padding:0}
html,body{width:1200px;height:3231px;overflow:hidden}
body{position:relative;font-family:"Roboto",Arial,sans-serif;color:var(--text);background:var(--white)}
.abs{position:absolute}
.serif{font-family:"Libre Caslon Text",Georgia,serif}

/* header */
.site-header{position:absolute;left:0;top:0;width:1200px;height:90px;background:var(--white);border-top:3px solid var(--blue);z-index:3}
.brand-tab{position:absolute;left:73px;top:-30px;width:190px;height:188px;border-radius:50%;background:var(--white);z-index:4;display:flex;align-items:center;justify-content:center;text-align:center}
.brand-name{font-family:"Roboto",Arial,sans-serif;font-weight:500;font-size:19px;line-height:1.2;color:var(--purple-light);margin-top:30px}
.main-nav{position:absolute;left:288px;top:36px;display:flex;font-size:15px;color:#333;z-index:5}
.main-nav span{margin-right:22px}
.main-nav .sep{color:#555}
.main-nav .active{color:var(--purple)}
.btn{display:inline-flex;align-items:center;justify-content:center;border-radius:22px;color:var(--white);font-weight:700;font-size:15px;text-transform:uppercase}
.btn-enquire{position:absolute;left:784px;top:25px;width:146px;height:40px;background:var(--purple);z-index:5}
.btn-info{position:absolute;left:937px;top:25px;width:184px;height:40px;background:var(--blue);z-index:5}
.btn svg{margin-left:10px}

/* hero */
.hero{position:absolute;left:0;top:90px;width:1200px;height:653px;background:linear-gradient(100deg,#2f4e1c 0%,#5d7f34 35%,#8ea56a 60%,#6f8f40 80%,#3d5c22 100%)}
.hero-shade{position:absolute;inset:0;background:linear-gradient(90deg,rgba(0,0,0,.35),rgba(0,0,0,0) 55%)}
.hero-copy{position:absolute;left:110px;top:195px;color:var(--white)}
.hero-kicker{font-size:42px;font-weight:700;line-height:1}
.hero-title{font-size:70px;font-weight:700;line-height:1;margin-top:16px}
.hero-lead{font-size:17px;font-weight:500;line-height:25px;margin-top:18px;width:450px}
.btn-start{margin-top:26px;width:167px;height:40px;background:var(--blue)}

/* benefits */
.section-title{position:absolute;width:1200px;text-align:center;font-size:38px;color:var(--ink)}
.intro{position:absolute;width:1200px;text-align:center;font-size:15.5px;line-height:26px;color:#333}
.card{position:absolute;top:965px;width:379px;height:393px;background:var(--white);border-radius:18px;box-shadow:0 4px 22px rgba(0,0,0,.1);padding:26px 40px}
.card h3{font-size:20px;font-weight:500;color:var(--ink);margin-bottom:16px}
.card ul{list-style:none}
.card li{display:flex;align-items:center;font-size:15.5px;line-height:19px;color:#333;margin-bottom:17px}
.card li svg{flex:none;margin-right:12px}
.slider-arrow{position:absolute;top:1145px;width:35px;height:35px;border-radius:50%;background:#eee;display:flex;align-items:center;justify-content:center}

/* about band */
.about-band{position:absolute;left:0;top:1616px;width:1200px;height:564px;background:linear-gradient(180deg,#8b4ce6 0%,#6d25d8 55%,#5a16cc 100%)}
.about-art{position:absolute;left:113px;top:74px;width:402px;height:400px;border-radius:50% 50% 40% 40%;background:radial-gradient(circle at 50% 55%,#d9d2c0 0%,#a5a386 45%,rgba(110,37,216,0) 72%)}
.about-copy{position:absolute;left:594px;top:64px;width:495px;color:var(--white)}
.about-copy h2{font-size:36px;line-height:41px;font-weight:400}
.about-copy p{font-size:15.5px;line-height:25.5px;text-align:justify;margin-top:14px}
.btn-learn{margin-top:22px;width:167px;height:40px;background:var(--blue)}

/* contact */
.contact{position:absolute;left:0;top:2180px;width:1200px;height:570px;background:linear-gradient(180deg,#fbfbfb 0%,#f3f3f2 70%,#e9ebe6 100%)}
.field{position:absolute;height:46px;border:1px solid var(--line);border-radius:24px;background:var(--white);display:flex;align-items:center;padding-left:28px;font-size:13px;color:#333}
.field svg{margin-right:12px}
.field-area{align-items:flex-start;padding-top:22px;border-radius:26px}
.btn-submit{position:absolute;left:517px;top:2625px;width:166px;height:40px;background:var(--blue)}

/* footer */
.site-footer{position:absolute;left:0;top:2750px;width:1200px;height:481px;background:var(--footer);color:var(--white)}
.footer-brand{position:absolute;left:110px;top:120px;font-size:24px;font-weight:500;color:var(--white)}
.footer-col{position:absolute;top:78px}
.footer-col h4{font-size:18px;font-weight:500}
.footer-col .rule{width:30px;height:2px;background:var(--purple-light);margin-top:12px}
.contact-line{display:flex;align-items:center;margin-top:24px}
.dot-icon{flex:none;width:28px;height:28px;border-radius:50%;background:var(--blue);display:flex;align-items:center;justify-content:center;margin-right:18px}
.newsletter{margin-top:20px;font-size:14px;line-height:19px;width:290px}
.subscribe{margin-top:18px;width:298px;height:46px;border-radius:24px;background:var(--white);border:2px solid var(--white);position:relative;display:flex;align-items:center;padding-left:18px;font-size:12px;color:#666}
.subscribe .btn{position:absolute;right:0;top:0;width:112px;height:42px;background:var(--blue);font-size:12px}
.social{display:flex;margin-top:14px}
.social span{width:33px;height:33px;border-radius:50%;background:var(--blue);margin-right:9px}
.footer-rule{position:absolute;left:110px;top:349px;width:977px;height:1px;background:#444}
.footer-nav{position:absolute;top:382px;width:1200px;display:flex;justify-content:center;font-size:15px}
.footer-nav span{margin:0 12px}
.copyright{position:absolute;top:428px;width:1200px;text-align:center;font-size:13.5px}
</style>
</head>
<body>

<header class="site-header">
  <nav class="main-nav">
    <span class="active">HOME</span><span class="sep">/</span>
    <span>ABOUT</span><span class="sep">/</span>
    <span>CLASSES</span><span class="sep">/</span>
    <span>BLOG</span><span class="sep">/</span>
    <span>CONTACT</span>
  </nav>
  <a class="btn btn-enquire">Enquire Now</a>
  <a class="btn btn-info">More Information</a>
</header>
<div class="brand-tab"><div class="brand-name">SunMeadow<br>Yoga</div></div>

<section class="hero" role="img" aria-label="Photo of a woman meditating cross-legged on a mat in a green park">
  <div class="hero-shade"></div>
  <div class="hero-copy">
    <div class="hero-kicker serif">Welcome To</div>
    <h1 class="hero-title serif">SunMeadow Yoga</h1>
    <p class="hero-lead">SunMeadow Yoga believe that you are never too young to benefit from and fall in love with yoga.</p>
    <a class="btn btn-start">Get Started
      <svg width="15" height="15" viewBox="0 0 16 16"><circle cx="8" cy="8" r="8" fill="#fff"/><path d="M5 8h5M8 5l3 3-3 3" stroke="#00a6df" stroke-width="2" fill="none"/></svg></a>
  </div>
</section>

<h2 class="section-title serif" style="top:820px">Benefits of Yoga</h2>
<p class="intro" style="top:877px">The benefits of yoga can last a lifetime. It is my aim &amp; passion to introduce yoga to kids of all ages and backgrounds<br>so that they can not only experience the benefits of yoga but fall in love with the practice.</p>

<div class="slider-arrow" style="left:111px"><svg width="10" height="12" viewBox="0 0 10 12"><path d="M7 1 2 6l5 5" stroke="#333" stroke-width="2" fill="none"/></svg></div>
<div class="slider-arrow" style="left:1051px"><svg width="10" height="12" viewBox="0 0 10 12"><path d="M3 1l5 5-5 5" stroke="#333" stroke-width="2" fill="none"/></svg></div>

<article class="card" style="left:200px">
  <h3>Healthy Minds</h3>
  <ul>
    <li><svg width="15" height="15" viewBox="0 0 16 16"><circle cx="8" cy="8" r="8" fill="#00a6df"/><path d="M4.5 8.2 7 10.5l4.5-4.8" stroke="#fff" stroke-width="2" fill="none"/></svg>Cultivates confidence and self-esteem</li>
    <li><svg width="15" height="15" viewBox="0 0 16 16"><circle cx="8" cy="8" r="8" fill="#00a6df"/><path d="M4.5 8.2 7 10.5l4.5-4.8" stroke="#fff" stroke-width="2" fill="none"/></svg>Develops concentration and attention</li>
    <li><svg width="15" height="15" viewBox="0 0 16 16"><circle cx="8" cy="8" r="8" fill="#00a6df"/><path d="M4.5 8.2 7 10.5l4.5-4.8" stroke="#fff" stroke-width="2" fill="none"/></svg>Clears the mind for better clarity and decision making</li>
    <li><svg width="15" height="15" viewBox="0 0 16 16"><circle cx="8" cy="8" r="8" fill="#00a6df"/><path d="M4.5 8.2 7 10.5l4.5-4.8" stroke="#fff" stroke-width="2" fill="none"/></svg>Helps relax and sleep better</li>
    <li><svg width="15" height="15" viewBox="0 0 16 16"><circle cx="8" cy="8" r="8" fill="#00a6df"/><path d="M4.5 8.2 7 10.5l4.5-4.8" stroke="#fff" stroke-width="2" fill="none"/></svg>Calms the nervous system</li>
    <li><svg width="15" height="15" viewBox="0 0 16 16"><circle cx="8" cy="8" r="8" fill="#00a6df"/><path d="M4.5 8.2 7 10.5l4.5-4.8" stroke="#fff" stroke-width="2" fill="none"/></svg>Learns to cope with stressful situations</li>
    <li><svg width="15" height="15" viewBox="0 0 16 16"><circle cx="8" cy="8" r="8" fill="#00a6df"/><path d="M4.5 8.2 7 10.5l4.5-4.8" stroke="#fff" stroke-width="2" fill="none"/></svg>Balances emotions</li>
  </ul>
</article>

<article class="card" style="left:620px">
  <h3>Healthy Spirits</h3>
  <ul>
    <li><svg width="15" height="15" viewBox="0 0 16 16"><circle cx="8" cy="8" r="8" fill="#00a6df"/><path d="M4.5 8.2 7 10.5l4.5-4.8" stroke="#fff" stroke-width="2" fill="none"/></svg>Fosters creativity, expression and imagination</li>
    <li><svg width="15" height="15" viewBox="0 0 16 16"><circle cx="8" cy="8" r="8" fill="#00a6df"/><path d="M4.5 8.2 7 10.5l4.5-4.8" stroke="#fff" stroke-width="2" fill="none"/></svg>Cultivates kindness to themselves and others</li>
    <li><svg width="15" height="15" viewBox="0 0 16 16"><circle cx="8" cy="8" r="8" fill="#00a6df"/><path d="M4.5 8.2 7 10.5l4.5-4.8" stroke="#fff" stroke-width="2" fill="none"/></svg>Cultivates respect for self and others</li>
    <li><svg width="15" height="15" viewBox="0 0 16 16"><circle cx="8" cy="8" r="8" fill="#00a6df"/><path d="M4.5 8.2 7 10.5l4.5-4.8" stroke="#fff" stroke-width="2" fill="none"/></svg>Builds balance and inner quiet</li>
    <li><svg width="15" height="15" viewBox="0 0 16 16"><circle cx="8" cy="8" r="8" fill="#00a6df"/><path d="M4.5 8.2 7 10.5l4.5-4.8" stroke="#fff" stroke-width="2" fill="none"/></svg>Builds inner strength and resilience</li>
    <li><svg width="15" height="15" viewBox="0 0 16 16"><circle cx="8" cy="8" r="8" fill="#00a6df"/><path d="M4.5 8.2 7 10.5l4.5-4.8" stroke="#fff" stroke-width="2" fill="none"/></svg>Teaches self-awareness</li>
    <li><svg width="15" height="15" viewBox="0 0 16 16"><circle cx="8" cy="8" r="8" fill="#00a6df"/><path d="M4.5 8.2 7 10.5l4.5-4.8" stroke="#fff" stroke-width="2" fill="none"/></svg>Focuses on positive self-talk</li>
  </ul>
</article>

<p class="intro" style="top:1406px">SunMeadow Yoga combines all the benefits of traditional yoga and a lot of fun!&nbsp; We play games and practice engaging flows which<br>get our bodies moving, then we take a quiet moment to be still and calm as we focus on our breathing.</p>
<p class="intro" style="top:1483px">SunMeadow Yoga Kids will learn that relaxation is just as important as moving their bodies, and the exercises which they learn in<br>class can easily be repeated at any time in their busy day to feel calm and grounded.</p>

<section class="about-band">
  <div class="about-art" role="img" aria-label="Yoga symbol artwork filled with a photo of a child meditating on grass"></div>
  <div class="about-copy">
    <h2 class="serif">Welcome to<br>SunMeadow Yoga</h2>
    <p>SunMeadow Yoga believe that you are never too young to benefit from and fall in love with yoga. My aim is to EMPOWER kids and teens to thrive by teaching life skills in Yoga, Mindfulness and Breathing techniques to deal with daily challenges and big emotions</p>
    <p>SunMeadow Yoga gives kids an opportunity to enjoy and experience yoga for themselves and primarily focuses on programs for Schools, Pre Schools and Early Learning Centres, Private Classes, Sporting Clubs, Martial Arts Schools, Scout Groups and Occupational Therapy Centres just to name a few. All classes are age appropriate and encourage children's natural drive to learn, move, and be creative.</p>
    <a class="btn btn-learn">Learn More
      <svg width="15" height="15" viewBox="0 0 16 16"><circle cx="8" cy="8" r="8" fill="#fff"/><path d="M5 8h5M8 5l3 3-3 3" stroke="#00a6df" stroke-width="2" fill="none"/></svg></a>
  </div>
</section>

<section class="contact" role="img" aria-label="Faint photo of a person in a tree pose outdoors"></section>
<h2 class="section-title serif" style="top:2256px">Contact Us</h2>
<div class="field" style="left:158px;top:2333px;width:438px"><svg width="12" height="12" viewBox="0 0 12 12"><circle cx="6" cy="3.5" r="3" fill="#222"/><path d="M0 12c0-4 3-5.5 6-5.5s6 1.5 6 5.5z" fill="#222"/></svg>First Name</div>
<div class="field" style="left:605px;top:2333px;width:438px"><svg width="12" height="12" viewBox="0 0 12 12"><circle cx="6" cy="3.5" r="3" fill="#222"/><path d="M0 12c0-4 3-5.5 6-5.5s6 1.5 6 5.5z" fill="#222"/></svg>Last Name</div>
<div class="field" style="left:158px;top:2397px;width:438px"><svg width="13" height="10" viewBox="0 0 13 10"><rect width="13" height="10" rx="1" fill="#222"/><path d="M1 1.5 6.5 5.5 12 1.5" stroke="#fff" stroke-width="1.2" fill="none"/></svg>Email</div>
<div class="field" style="left:605px;top:2397px;width:438px"><svg width="8" height="12" viewBox="0 0 8 12"><rect x=".5" y=".5" width="7" height="11" rx="1" fill="none" stroke="#222"/><rect x="2" y="2" width="4" height="7" fill="#222"/></svg>Phone</div>
<div class="field field-area" style="left:158px;top:2460px;width:885px;height:121px"><svg width="14" height="11" viewBox="0 0 14 11"><ellipse cx="5.5" cy="4" rx="5.5" ry="4" fill="#222"/><ellipse cx="9.5" cy="6.5" rx="4.5" ry="3.5" fill="#222"/></svg>Comments</div>
<a class="btn btn-submit">Submit Now
  <svg width="15" height="15" viewBox="0 0 16 16"><circle cx="8" cy="8" r="8" fill="#fff"/><path d="M5 8h5M8 5l3 3-3 3" stroke="#00a6df" stroke-width="2" fill="none"/></svg></a>

<footer class="site-footer">
  <div class="footer-brand">SunMeadow Yoga</div>
  <div class="footer-col" style="left:418px">
    <h4>Address</h4><div class="rule"></div>
    <div class="contact-line" style="font-size:14px;font-weight:700;line-height:23px"><span class="dot-icon"><svg width="10" height="13" viewBox="0 0 10 13"><path d="M5 0a5 5 0 0 1 5 5c0 3.5-5 8-5 8S0 8.5 0 5a5 5 0 0 1 5-5z" fill="#fff"/><circle cx="5" cy="5" r="1.8" fill="#00a6df"/></svg></span>122,Lorem ipsum dolor sit<br>consectetur adipiscing</div>
    <div class="contact-line" style="font-size:19px;font-weight:700"><span class="dot-icon"><svg width="12" height="12" viewBox="0 0 12 12"><path d="M2.5 0 5 3 3.8 4.5a7 7 0 0 0 3.7 3.7L9 7l3 2.5-1.5 2C5 12 0 7 .5 1.5z" fill="#fff"/></svg></span>0400 318 265</div>
    <div class="contact-line" style="font-size:15px"><span class="dot-icon"><svg width="12" height="9" viewBox="0 0 12 9"><rect width="12" height="9" rx="1" fill="#fff"/><path d="M1 1 6 5l5-4" stroke="#00a6df" fill="none"/></svg></span>hello@sunmeadowyoga.example/</div>
  </div>
  <div class="footer-col" style="left:785px">
    <h4>Subscribe Newsletter</h4><div class="rule"></div>
    <p class="newsletter">Lorem ipsum dolor sit amet, consectetur adipiscing elit, sed do eiusmod</p>
    <div class="subscribe"><svg width="13" height="10" viewBox="0 0 13 10" style="margin-right:8px"><rect width="13" height="10" rx="1" fill="#666"/><path d="M1 1.5 6.5 5.5 12 1.5" stroke="#fff" stroke-width="1.2" fill="none"/></svg>Email Address *<span class="btn">Subscribe</span></div>
    <h4 style="margin-top:20px">Follow Us On</h4><div class="rule"></div>
    <div class="social"><span></span><span></span></div>
  </div>
  <div class="footer-rule"></div>
  <nav class="footer-nav"><span>HOME</span><span>/</span><span>ABOUT</span><span>/</span><span>CLASSES</span><span>/</span><span>BLOG</span><span>/</span><span>CONTACT</span></nav>
  <p class="copyright">Copyright 2023 SunMeadow Yoga</p>
</footer>

</body>
</html>
```